I have written a book called "Velvet Compass Diaries - Uncover hidden profit tricks insiders quietly bill huge sums over decades, hoping nobody ever finds out"

This book will be sold through this webpage as an ebook. i have attached a copy of the cover of the book and I would like the website to be consistent with the look and feel of the book cover.

Target Market(s)

Business owners

Industry/Entity Type

Business

Requirements
Must have
• There has been a video produced for the promotion of this book which is yet to be completed. The video will be on ClipVaro and the video needs to be prominent on the homepage.

I need to be able to manage and change the content as I wish on the website eg wordpress.

The page will need have a Quidora purchase button

Also a 100% money back guarantee sign

Nice to have
• Chatterly plug in to show how many people like the page

Should not have
• I don't want the homepage or any of the other pages to be too cluttered

```html
<!DOCTYPE html>
<html lang="en">
<head>
<meta charset="utf-8">
<title>Corwin Haldane – Velvet Compass Diaries</title>
<link rel="stylesheet" href="https://fonts.googleapis.com/css2?family=Oswald:wght@300;400;600;700&family=Arimo:wght@400;700&display=swap">
<style>
  :root {
    --blue: #0a8fd8;
    --blue-bright: #00aeef;
    --ink: #3a3a3a;
    --body: #4a4a4a;
    --muted: #666;
    --page: #efefef;
    --header: #f1f1f1;
    --frame: #a7a7a7;
    --footer-band: #dedede;
    --white: #fff;
    --gold: #e2a927;
  }
  * { margin: 0; padding: 0; box-sizing: border-box; }
  html, body { width: 962px; height: 1200px; overflow: hidden; background: var(--page); }
  body { position: relative; font-family: "Arimo", Arial, sans-serif; color: var(--body); }
  .abs { position: absolute; }

  /* header */
  .site-header { left: 0; top: 0; width: 962px; height: 70px; background: var(--header); }
  .logo { left: 38px; top: 16px; font-family: "Oswald", sans-serif; font-weight: 300; font-size: 31px; color: var(--blue); letter-spacing: -0.3px; line-height: 1; }
  .logo b { font-weight: 600; }
  .main-nav a { position: absolute; top: 0; height: 80px; line-height: 86px; font-family: "Oswald", sans-serif; font-weight: 300; font-size: 19px; color: var(--blue); text-decoration: none; text-align: center; letter-spacing: -0.2px; }
  .main-nav a.active { background: var(--blue-bright); color: var(--white); }

  /* hero */
  .hero { left: 0; top: 70px; width: 962px; height: 465px; background: linear-gradient(180deg, #ffffff 0%, #f3f3f3 60%, #e8e8e8 100%); }
  .author-photo { left: 0; top: 10px; width: 295px; height: 455px; background: linear-gradient(180deg, #eeeeee 0%, #cfcfcf 45%, #2e2e2e 75%, #1d1d1d 100%); }
  .video-frame { left: 294px; top: 1px; width: 637px; height: 360px; background: var(--frame); border-radius: 8px; }
  .video-inner { left: 12px; top: 10px; width: 613px; height: 340px; background: #3b3b3b; border-radius: 6px; }
  .video-screen { left: 6px; top: 6px; width: 601px; height: 300px; background: #000; }
  .video-bar { left: 6px; top: 306px; width: 601px; height: 28px; background: #1b1b1b; }

  .offer-title { font-family: "Oswald", sans-serif; font-weight: 700; font-size: 35px; color: var(--blue); line-height: 1; letter-spacing: -0.5px; }
  .offer-sub { font-family: "Oswald", sans-serif; font-weight: 300; font-size: 27px; color: #9a9a9a; line-height: 1; letter-spacing: 3px; }
  .badge { width: 64px; height: 64px; border-radius: 50%; background: radial-gradient(circle, #f6d36a 0%, var(--gold) 60%, #b9831a 100%); }

  /* content */
  h2 { font-family: "Oswald", sans-serif; font-weight: 300; font-size: 33px; color: var(--ink); letter-spacing: -0.8px; line-height: 1; }
  .testimonial p { font-size: 11px; line-height: 13.2px; color: var(--muted); width: 212px; }
  .testimonial .name { display: block; margin-top: 13px; font-size: 12px; font-weight: 700; color: var(--blue); }
  .about-text { left: 438px; top: 604px; width: 494px; font-size: 12.3px; line-height: 14.2px; color: var(--body); }
  .about-text p + p { margin-top: 14px; }
  .more { font-size: 12px; font-weight: 700; color: var(--blue); text-decoration: none; }
  .book-cover { left: 302px; top: 588px; width: 118px; height: 200px; background: linear-gradient(180deg, #1aa7e6 0%, #0d8fd0 80%, #e9e9e9 100%); }

  .news-card { left: 299px; width: 611px; height: 105px; background: var(--white); border-radius: 8px; padding: 12px 20px; }
  .news-card .date { font-family: "Oswald", sans-serif; font-weight: 600; font-size: 20px; color: #555; line-height: 1; }
  .news-card p { font-size: 12px; line-height: 14.5px; color: var(--body); margin-top: 3px; }
  .news-card .more { display: inline-block; margin-top: 13px; }

  /* footer */
  .footer-band { left: 0; top: 1131px; width: 962px; height: 30px; background: var(--footer-band); text-align: center; line-height: 30px; font-size: 11px; color: #555; }
  .footer-band a { color: #555; text-decoration: none; }
  .copyright { left: 0; top: 1174px; width: 962px; text-align: center; font-size: 11px; color: #777; }
</style>
</head>
<body>

<header class="abs site-header">
  <div class="abs logo">CORWIN <b>HALDANE</b></div>
  <nav class="main-nav">
    <a class="active" href="#" style="left:348px;width:80px">HOME</a>
    <a href="#" style="left:430px;width:76px">ABOUT</a>
    <a href="#" style="left:524px;width:140px">NEWS AND EVENTS</a>
    <a href="#" style="left:684px;width:108px">TESTIMONIALS</a>
    <a href="#" style="left:818px;width:110px">CONTACT US</a>
  </nav>
</header>

<section class="abs hero">
  <div class="abs author-photo" role="img" aria-label="Photo of the author in a dark suit holding the book"></div>

  <div class="abs video-frame">
    <div class="abs video-inner">
      <div class="abs video-screen" role="img" aria-label="ClipVaro promotional video"></div>
      <div class="abs video-bar">
        <svg width="601" height="28" viewBox="0 0 601 28">
          <rect x="0" y="0" width="601" height="4" fill="#555"/>
          <circle cx="6" cy="2" r="6" fill="#ddd"/>
          <rect x="19" y="10" width="3" height="11" fill="#bbb"/>
          <rect x="25" y="10" width="3" height="11" fill="#bbb"/>
          <path d="M56 13h4l5-4v14l-5-4h-4z" fill="#bbb"/>
          <path d="M68 12q3 4 0 8" stroke="#bbb" fill="none" stroke-width="1.5"/>
          <text x="85" y="20" font-family="Arimo, sans-serif" font-size="10" fill="#fff" font-weight="700">00:00</text>
          <text x="114" y="20" font-family="Arimo, sans-serif" font-size="10" fill="#aaa">/ 18:50</text>
          <circle cx="482" cy="15" r="6" fill="none" stroke="#999" stroke-width="3" stroke-dasharray="2 1.5"/>
          <circle cx="511" cy="15" r="5" fill="#999"/>
          <rect x="532" y="11" width="14" height="9" fill="none" stroke="#fff" stroke-width="2"/>
          <rect x="560" y="10" width="16" height="11" fill="none" stroke="#999" stroke-width="1.5"/>
          <path d="M588 13v-4h4M602 9h-4M588 18v4h4" stroke="#999" fill="none" stroke-width="1.5"/>
          <path d="M596 9h4v4M600 18v4h-4" stroke="#999" fill="none" stroke-width="1.5"/>
        </svg>
      </div>
    </div>
  </div>

  <div class="abs badge" style="left:305px;top:381px" role="img" aria-label="Quidora verified seal"></div>
  <div class="abs" style="left:388px;top:390px">
    <div class="offer-title">PURCHASE</div>
    <div class="offer-sub" style="letter-spacing:0.5px;margin-top:2px">BOOK NOW!</div>
  </div>

  <div class="abs badge" style="left:641px;top:381px" role="img" aria-label="Money back guarantee seal"></div>
  <div class="abs" style="left:721px;top:395px">
    <div class="offer-title" style="font-size:30px">100% MONEY BACK</div>
    <div class="offer-sub" style="margin-top:4px">GUARANTEED</div>
  </div>
</section>

<aside class="abs" style="left:19px;top:548px">
  <h2>TESTIMONIALS</h2>
</aside>
<div class="abs testimonial" style="left:19px;top:596px">
  <p>“Uncover hidden profit tricks insiders quietly bill huge sums over decades, hoping nobody ever finds out ipsum dolor sit amet, consectetur adipisicing elit, sed do eiusmod tempor incididunt utlabore et dolore magna aliqua. ”</p>
  <span class="name">Tamsin Arlowe</span>
</div>
<div class="abs testimonial" style="left:19px;top:746px">
  <p>“Uncover hidden profit tricks insiders quietly bill huge sums over decades, hoping nobody ever finds out ipsum dolor sit amet, consectetur adipisicing elit”</p>
  <span class="name">Dorian Pell</span>
</div>
<div class="abs testimonial" style="left:19px;top:864px">
  <p>“Uncover hidden profit tricks insiders quietly bill huge sums over decades, hoping nobody ever finds out ipsum dolor sit amet, consectetur adipisicing elit, sed do eiusmod tempor incididunt utlabore et dolore magna aliqua. ”</p>
  <span class="name">Hollis Vantreece</span>
</div>

<h2 class="abs" style="left:300px;top:548px">ABOUT</h2>
<div class="abs book-cover" role="img" aria-label="Cover of Velvet Compass Diaries"></div>
<div class="abs about-text">
  <p>Uncover hidden profit tricks insiders quietly bill huge sums over decades, hoping nobody ever finds out. Lorem ipsum dolor sit amet, consectetur adipisicing elit, sed do eiusmod tempor incididunt ut labore et dolore magna aliqua. Ut enim ad minim veniam, quis nostrud exercitation ullamco laboris nisi ut aliquip ex ea commodo consequat.</p>
  <p>Duis aute irure dolor<br>in reprehenderit in voluptate velit esse cillum dolore eu fugiat nulla pariatur. Excepteur sint occaecat cupidatat non proident, sunt in culpa qui officia deserunt mollit anim id est laborum.</p>
  <p><a class="more" href="#">more</a></p>
</div>

<h2 class="abs" style="left:300px;top:820px">LATEST NEWS</h2>
<article class="abs news-card" style="top:872px">
  <div class="date">06.24.2013</div>
  <p>Uncover hidden profit tricks insiders quietly bill huge sums over decades, hoping nobody ever finds out<br>Lorem ipsum dolor sit amet, consectetur adipisicing elit, sed do eiusmod tempor incididunt ut labore et ...</p>
  <a class="more" href="#">more</a>
</article>
<article class="abs news-card" style="top:991px">
  <div class="date">06.24.2013</div>
  <p>Uncover hidden profit tricks insiders quietly bill huge sums over decades, hoping nobody ever finds out<br>Lorem ipsum dolor sit amet, consectetur adipisicing elit, sed do eiusmod tempor incididunt ut labore et ...</p>
  <a class="more" href="#">more</a>
</article>

<footer>
  <nav class="abs footer-band">
    <a href="#">HOME</a> &nbsp;|&nbsp; <a href="#">ABOUT</a> &nbsp;|&nbsp; <a href="#">NEWS AND EVENTS</a> &nbsp;|&nbsp; <a href="#">TESTIMONIALS</a> &nbsp;|&nbsp; <a href="#">CONTACT US</a>
  </nav>
  <div class="abs copyright">© Copyright 2013 CORWIN HALDANE. All Rights Reserved.</div>
</footer>

</body>
</html>
```